Consulting company, design, Interior design in commercial real estate (Tertiai sector *

Company name: DORALYNE: from the Greek Evexia well-being, was born from a desire to combine well-being and work. By the choice of design, materials, design and furniture, everything is thought from this perspective

Logo: Essay with Möbius Ribbon and / or with the infinite acronym / and or triangle ...
Sentences to write:
"The exclusive partner for your development projects"
"Consulting - Design - Construction"
"We manage EVERYTHING for you"

On the back: Photo (attached; if photo is not clear, another photo can be provided) with company name and "DORALYNE, Excellence and reliability"
My name / First name: provided later (double name), Manager
Address: supplied later
Tel: supplied later
Website: www. doralyne.example
Colors: Black, gold and white. Other admissible colors
See attached files

Target Market(s)

Real estate business

Contact Information for Business Card

Nom de l'entreprise : DORALYNE : du grec Evexia bien être, est né d'une volonté de faire rimer bien être et travail. Par le choix de la conception, des matériaux, du design et du mobilier, tout est pensé dans cette optique

Logo : Essai avec Ruban de Möbius et /ou avec le sigle infini / et ou triangle...
Phrases à inscrire :
"Le partenaire exclusif de vos projets d'aménagement"
"Conseil - Conception - Construction"
"Nous gérons TOUT pour vous"

Au verso : Photo (ci-jointe ; si photo pas nette, une autre photo peut être fournie) avec nom de l'entreprise et Mention "DORALYNE, Excellence et fiabilité"
Mon nom / Prénom : fourni ultérieurement (prénom double), Gérant
Adresse : fourni ultérieurement
Tél : fourni ultérieurement
Site Web : www. doralyne.example
Couleurs : Noir, doré et blanc. Autre couleurs recevables
Voir fichiers ci-joint

Requirements
Must have
• My project must be simple, clear, neat and design.
The business card must catch the customer

```html
<!DOCTYPE html>
<html lang="en">
<head>
<meta charset="utf-8">
<title>DORALYNE business card</title>
<link rel="stylesheet" href="https://fonts.googleapis.com/css2?family=Montserrat:wght@800&family=Arimo:wght@400;700&display=swap">
<style>
  :root {
    --canvas: #d9d9d9;
    --charcoal: #2e2b2c;
    --gold: #f4a928;
    --gold-deep: #e9a21c;
    --ink: #1c1c1c;
    --white: #ffffff;
    --photo-top: #e7e3dc;
    --photo-bottom: #2c3448;
  }
  * { box-sizing: border-box; margin: 0; padding: 0; }
  html, body { width: 1200px; height: 1015px; overflow: hidden; }
  body {
    background: var(--canvas);
    font-family: "Arimo", Arial, sans-serif;
    display: flex;
    flex-direction: column;
    align-items: center;
    justify-content: center;
    gap: 40px;
  }
  .card {
    position: relative;
    width: 780px;
    height: 446px;
    overflow: hidden;
    box-shadow: 0 10px 30px rgba(0,0,0,.25);
  }
  .card::after {
    content: "";
    position: absolute;
    left: 0; right: 0; bottom: 0;
    height: 14px;
    background: var(--gold);
  }
  .card--front { background: var(--charcoal); }
  .card--back { background: var(--white); }

  .wordmark {
    position: absolute;
    font-family: "Montserrat", sans-serif;
    font-weight: 800;
    letter-spacing: 2px;
    line-height: 1;
    white-space: nowrap;
  }
  .card--front .wordmark {
    left: 50%; top: 50%;
    transform: translate(-50%, -60%);
    font-size: 72px;
    color: var(--white);
  }
  .card--back .wordmark {
    right: 50px; top: 70px;
    font-size: 50px;
    color: var(--ink);
  }

  .portrait {
    position: absolute;
    left: 60px; top: 66px;
    width: 262px; height: 196px;
    background: linear-gradient(170deg, var(--photo-top) 0%, #d8d2c8 55%, var(--photo-bottom) 100%);
  }
  .person { position: absolute; left: 60px; top: 276px; }
  .person__name {
    font-family: "Montserrat", sans-serif;
    font-weight: 800;
    font-size: 24px;
    color: var(--gold-deep);
    letter-spacing: .5px;
    white-space: nowrap;
  }
  .person__role { font-size: 19px; color: var(--ink); margin-top: 2px; }
  .contacts { list-style: none; margin-top: 12px; }
  .contacts li {
    display: flex; align-items: center; gap: 10px;
    font-size: 18px; color: var(--ink); line-height: 26px;
    white-space: nowrap;
  }
  .contacts svg { width: 18px; height: 18px; flex: none; }

  .pitch {
    position: absolute;
    right: 50px; top: 176px;
    text-align: right;
    font-size: 18px; line-height: 25px; color: var(--ink);
    white-space: nowrap;
  }
  .pitch .dot {
    display: inline-block; width: 8px; height: 8px; border-radius: 50%;
    background: var(--gold); margin-left: 6px; vertical-align: middle;
  }
  .address {
    position: absolute;
    right: 50px; top: 318px;
    text-align: right;
    font-size: 18px; line-height: 25px; color: var(--ink);
    white-space: nowrap;
  }
</style>
</head>
<body>
  <section class="card card--front">
    <div class="wordmark">DORALYNE</div>
  </section>

  <section class="card card--back">
    <div class="portrait" role="img" aria-label="Portrait photo of the managing director"></div>

    <div class="person">
      <div class="person__name">MARC-OLIVIER DURAND</div>
      <div class="person__role">Managing Director</div>
      <ul class="contacts">
        <li>
          <svg viewBox="0 0 24 24" aria-hidden="true"><path fill="var(--gold)" d="M6.6 10.8a15.2 15.2 0 0 0 6.6 6.6l2.2-2.2a1 1 0 0 1 1-.25 11.4 11.4 0 0 0 3.6.57 1 1 0 0 1 1 1V20a1 1 0 0 1-1 1A17 17 0 0 1 3 4a1 1 0 0 1 1-1h3.5a1 1 0 0 1 1 1c0 1.25.2 2.45.57 3.57a1 1 0 0 1-.25 1z"/></svg>
          044-555 010 274
        </li>
        <li>
          <svg viewBox="0 0 24 24" aria-hidden="true"><rect x="2" y="5" width="20" height="14" fill="var(--gold)"/><path d="M2 5l10 8 10-8" fill="none" stroke="var(--white)" stroke-width="1.8"/></svg>
          contact@doralyne.example
        </li>
        <li>
          <svg viewBox="0 0 24 24" aria-hidden="true"><g fill="none" stroke="var(--gold)" stroke-width="2"><circle cx="12" cy="12" r="9.5"/><ellipse cx="12" cy="12" rx="4" ry="9.5"/><path d="M2.5 12h19M4 7h16M4 17h16"/></g></svg>
          www.doralyne.example
        </li>
      </ul>
    </div>

    <div class="wordmark">DORALYNE</div>

    <p class="pitch">
      The exclusive partner for<span class="dot"></span><br>
      your development projects<br>
      Consulting - Design - Construction<span class="dot"></span><br>
      We manage EVERYTHING for you<span class="dot"></span>
    </p>

    <p class="address">
      18, Rue des Ateliers<br>
      Lyon, 69003
    </p>
  </section>
</body>
</html>
```